Interior Design business card design

I am an interior decorator - dont want to specify decorating more just design.
Want organic looking logo - charcoal and white - with touch of lime green.
Like the idea of some sort of spiral in corner but writing in a line
want lower case, carlamintowe as one and designs in different font underneath. Maybe using c and m as logo.
More modern than traditional. My clients are mid to top end residential

Target Market(s)

medium to top end homeowners

Industry/Entity Type

Residential

Contact Information for Business Card

Carla Mintowe Designs
58 Fallowmere ave
Tindarra 2188 NSW
Tel 0417869214
carlamintowe@quellnet.com.au

Logo Text

Carla Mintowe Designs

Logo styles of interest
Abstract Logo
Lettermark Logo
Requirements
Must have
• Name address ph and e mail
Nice to have
• Contemporary
smart but organic
Should not have
• no traditional fonts

```html
<!DOCTYPE html>
<html lang="en">
<head>
<meta charset="utf-8">
<title>Carla Mintowe Designs — Business Card</title>
<link rel="stylesheet" href="https://fonts.googleapis.com/css2?family=Lexend:wght@300;400&display=swap">
<style>
  :root {
    --charcoal: #3a3a44;
    --ink: #2a2a30;
    --lime: #4cb848;
    --card-edge: #55555c;
    --paper: #ffffff;
    --vignette: #ececef;
  }
  html, body {
    margin: 0;
    padding: 0;
    width: 1200px;
    height: 1000px;
    overflow: hidden;
    background: var(--paper);
    font-family: "Lexend", sans-serif;
  }
  .canvas {
    position: relative;
    width: 1200px;
    height: 1000px;
  }
  .card {
    position: absolute;
    left: 234px;
    top: 272px;
    width: 745px;
    height: 430px;
    border: 1px solid var(--card-edge);
    background: var(--paper);
    box-sizing: border-box;
  }
  .card-art {
    position: absolute;
    left: 0;
    top: 0;
    width: 100%;
    height: 100%;
  }
  .brand-name {
    position: absolute;
    left: 145px;
    top: 74px;
    margin: 0;
    color: var(--charcoal);
    font-family: "Lexend", sans-serif;
    font-weight: 400;
    font-size: 30px;
    line-height: 40px;
    letter-spacing: 0.2px;
  }
  .brand-name span { display: block; }
  .address, .contact {
    position: absolute;
    left: 67px;
    margin: 0;
    color: var(--ink);
    font-size: 22px;
    line-height: 32px;
    letter-spacing: 0.6px;
  }
  .address { top: 194px; font-weight: 300; }
  .contact { top: 318px; font-weight: 400; }
  .contact .label { font-weight: 300; }
  .address span, .contact span.line { display: block; }
</style>
</head>
<body>
<div class="canvas">
  <div class="card">
    <svg class="card-art" width="745" height="430" viewBox="0 0 745 430" aria-hidden="false">
      <!-- brand circle -->
      <circle class="brand-mark" cx="92" cy="112" r="40" fill="none" stroke="var(--lime)" stroke-width="3"/>
      <!-- shelf line -->
      <line x1="67" y1="161" x2="496" y2="161" stroke="var(--charcoal)" stroke-width="2.5"/>
      <line x1="676" y1="161" x2="745" y2="161" stroke="var(--charcoal)" stroke-width="2.5"/>
      <!-- furniture vignette area -->
      <rect class="furniture-vignette" x="496" y="118" width="180" height="72" rx="4" fill="var(--vignette)" role="img" aria-label="Line illustration of furniture and a potted plant sitting on the shelf line"/>
    </svg>

    <h1 class="brand-name">
      <span>carla mintowe</span>
      <span>designs</span>
    </h1>

    <p class="address">
      <span>58 Fallowmere Ave</span>
      <span>Tindarra 2188 NSW</span>
    </p>

    <p class="contact">
      <span class="line"><span class="label">Tel</span> 0417869214</span>
      <span class="line">carlamintowe@quellnet.com.au</span>
    </p>
  </div>
</div>
</body>
</html>
```